Northcliff Thermal Services Ltd Needs a 2 sided A5 Flyer Design

We need a flyer design for our company to promote Air and ground Source Heat Pumps in the Devon and Cornwall region of the UK.

Our Government has launched the DWB (domestic warmth bonus) a 7 year quarterly payment to offset the cost of installation..
Homeowners currently using OIL or LPG gas for there heating and hot water will save up to 50% on there energy bill by swapping to a heat pump,
Currently education is needed to the potential end user on the benefits of heat pumps,
This flyer will be part of an initial start point to get the homeowner to book a free survey to discuss there options, We are a renewable energy company with great local knowledge, and a wealth of experience ......

KEY points SAVINGS OF UP TO 50% on OIL or LPG heating and hot water systems

DWB PAYMENTS FROM GOVERNMENT FOR 7 years

HONEST IMPARTIAL ADVICE ON SOLUTIONS

FREE SURVEYS ON ALL RENEWABLE SOLUTIONS AND COSTINGS. website www.ncthermal.co.uk have included some potential wording

LOGOS FROM SUPPLIERS

We think side one should be high impact on high oil and LPG gas costs, harm to environment and potential 50% savings with a heat pump. Side 2 to be DWB 7 year quarterly payment and a little about our company offering expertise and free impartial advice and survey

general theme a "striking call to action"

Target Market(s)

Target market is 40 to 60 year old home owners that are off gas grid and use oil or LPG for heating and hot water

Industry/Entity Type

Environment

Font styles to use
Serif
Sans Serif

Colors
33a6d7
f04a50
00a88f
fbed22

Requirements
Must have
• savings 50% on oil or LPG energy costs for heating and hot water

DWB (domestic warmth bonus) government backed payments to offset cost of instalation

7 year payments averaging £1000 a year

FREE impartial advice and surveys

```html
<!DOCTYPE html>
<html lang="en">
<head>
<meta charset="utf-8">
<title>Northcliff Thermal Services – Heat Pump Flyer</title>
<link rel="stylesheet" href="https://fonts.googleapis.com/css2?family=Open+Sans:wght@400;600;700;800&display=swap">
<style>
  :root{
    --red:#e42a2f;
    --green:#3f8b2c;
    --green-dark:#2f6e1f;
    --green-field:#5c9e2c;
    --text-dark:#2b2b2b;
    --text-panel:#444;
    --panel-white:rgba(255,255,255,0.82);
    --sky-top:#5a9fd0;
    --sky-low:#cfe3f1;
    --url-green:#3c8a2a;
  }
  *{margin:0;padding:0;box-sizing:border-box}
  html,body{width:1200px;height:844px;overflow:hidden;background:#fff}
  body{position:relative;font-family:"Open Sans",Arial,sans-serif}

  .page{position:absolute;top:38px;width:542px;height:768px;overflow:hidden}
  .page--front{left:42px}
  .page--back{left:616px;border:1px solid #d6d6d6}

  /* Front */
  .front-art{position:absolute;inset:0}
  .no-badge{position:absolute;left:176px;top:22px;width:190px;height:190px;border-radius:50%;
    background:var(--red);border:7px solid #fff;box-shadow:0 0 0 4px var(--red);
    display:flex;flex-direction:column;align-items:center;justify-content:center;color:#fff;text-align:center}
  .no-badge__big{font-weight:800;font-size:62px;line-height:0.95}
  .no-badge__small{font-weight:800;font-size:27px;line-height:1.0}
  .rosette{position:absolute;left:178px;top:270px;width:78px;height:78px;border-radius:50%;
    background:#4e9a2f;border:4px solid #8bc34a}
  .yes-box{position:absolute;left:16px;top:332px;width:186px;height:236px;background:var(--green);
    color:#fff;padding:10px 0 0 22px}
  .yes-box__lead{font-weight:700;font-size:36px;line-height:1.1}
  .yes-box__line{font-weight:700;font-size:29px;line-height:1.15;letter-spacing:0.5px}
  .benefits{position:absolute;left:202px;top:374px;width:320px;height:194px;background:var(--panel-white);
    padding:30px 0 0 20px;list-style:none}
  .benefit{display:flex;align-items:flex-start;margin-bottom:14px}
  .benefit__icon{width:52px;flex:none;margin-top:-2px}
  .benefit__text{font-weight:600;font-size:13.5px;line-height:1.22;color:var(--text-panel);text-transform:uppercase}
  .intro{position:absolute;left:18px;top:568px;width:505px;height:142px;background:rgba(255,255,255,0.72);
    padding:18px 14px 0 14px;font-size:14.5px;line-height:1.25;color:var(--text-panel)}
  .intro p+p{margin-top:18px}

  /* Back */
  .back-art{position:absolute;inset:0}
  .brand{position:absolute;left:201px;top:17px;width:140px;height:54px;background:#fff;border-radius:9px;
    display:flex;align-items:center;justify-content:center;gap:6px;padding:0 8px}
  .brand__mark{width:12px;height:12px;border-radius:50%;background:var(--green);flex:none}
  .brand__name{font-size:10.5px;font-weight:600;color:#3a3a3a;line-height:1.15;text-align:center}
  .back-copy{position:absolute;left:32px;top:197px;width:476px;color:#fff;font-size:11.3px;line-height:1.33}
  .back-copy p{margin-bottom:12px;text-align:justify}
  .back-footer{position:absolute;left:0;top:637px;width:542px;height:131px;background:#fff}
  .back-url{position:absolute;top:22px;width:100%;text-align:center;font-weight:700;font-size:22px;color:var(--url-green)}
  .partners{position:absolute;top:78px;left:32px;display:flex;align-items:center;gap:20px}
  .partner{display:block}
</style>
</head>
<body>

<section class="page page--front">
  <svg class="front-art" width="542" height="768" viewBox="0 0 542 768">
    <defs>
      <linearGradient id="iceTone" x1="0" y1="0" x2="1" y2="1">
        <stop offset="0" stop-color="#8a7a6e"/><stop offset="0.5" stop-color="#a79a93"/><stop offset="1" stop-color="#6d7f92"/>
      </linearGradient>
      <linearGradient id="skyTone" x1="0" y1="0" x2="0" y2="1">
        <stop offset="0" stop-color="var(--sky-top)"/><stop offset="0.6" stop-color="var(--sky-low)"/><stop offset="1" stop-color="#e8f0f4"/>
      </linearGradient>
      <linearGradient id="grassTone" x1="0" y1="0" x2="0" y2="1">
        <stop offset="0" stop-color="#b6d47a"/><stop offset="1" stop-color="#4f8a26"/>
      </linearGradient>
    </defs>
    <g role="img" aria-label="Blue sky with soft clouds above a field of young green crop">
      <rect width="542" height="768" fill="url(#skyTone)"/>
      <rect y="560" width="542" height="208" fill="url(#grassTone)"/>
    </g>
    <path role="img" aria-label="Frozen oil-stained puddle with broken reeds" d="M0 0H542V185C420 200 250 240 140 260C80 270 30 280 0 290Z" fill="url(#iceTone)"/>
    <path d="M0 290C30 280 80 270 140 260C250 240 420 200 542 185V200C420 222 260 260 150 282C80 296 30 305 0 318Z" fill="var(--green-dark)"/>
  </svg>

  <div class="no-badge">
    <span class="no-badge__big">NO</span>
    <span class="no-badge__small">TO OIL<br>&amp; LPG</span>
  </div>
  <div class="rosette" role="img" aria-label="Eco award rosette"></div>

  <div class="yes-box">
    <div class="yes-box__lead">YES TO</div>
    <div class="yes-box__line">AIR &amp;<br>GROUND<br>SOURCE<br>HEAT<br>PUMPS</div>
  </div>

  <ul class="benefits">
    <li class="benefit">
      <svg class="benefit__icon" width="44" height="44" viewBox="0 0 44 44">
        <circle cx="20" cy="18" r="15" fill="none" stroke="#333" stroke-width="2.5"/>
        <path d="M20 3A15 15 0 0 1 20 33Z" fill="#333"/>
        <text x="26" y="42" font-size="10" font-family="Open Sans, sans-serif" fill="#333">50%</text>
      </svg>
      <span class="benefit__text">Savings of 50% compared<br>to oil or LPG for heat and<br>hot water</span>
    </li>
    <li class="benefit">
      <svg class="benefit__icon" width="44" height="36" viewBox="0 0 44 36">
        <path d="M8 16A12 12 0 0 1 30 9" fill="none" stroke="#333" stroke-width="3"/>
        <path d="M27 3L33 10L25 12Z" fill="#333"/>
        <path d="M32 20A12 12 0 0 1 10 27" fill="none" stroke="#333" stroke-width="3"/>
        <path d="M13 33L7 26L15 24Z" fill="#333"/>
      </svg>
      <span class="benefit__text">Government backed DWB<br>domestic warmth bonus</span>
    </li>
    <li class="benefit">
      <svg class="benefit__icon" width="44" height="36" viewBox="0 0 44 36">
        <path d="M4 18L14 30L34 4" fill="none" stroke="#222" stroke-width="5" stroke-linecap="round"/>
      </svg>
      <span class="benefit__text">£1,000 a year payments on<br>average for 7 years<br>for instalation</span>
    </li>
  </ul>

  <div class="intro">
    <p>Air source heat pumps will fit into your current radiator heating system in most cases, and will provide all of your heating and hot water needs for the home.</p>
    <p>You will no longer have to pay for high priced Oil and LPG.</p>
  </div>
</section>

<section class="page page--back">
  <svg class="back-art" width="542" height="768" viewBox="0 0 542 768">
    <defs>
      <linearGradient id="backSky" x1="0" y1="0" x2="0" y2="1">
        <stop offset="0" stop-color="#4f95cf"/><stop offset="1" stop-color="#b9d6ec"/>
      </linearGradient>
      <linearGradient id="backField" x1="0" y1="0" x2="0" y2="1">
        <stop offset="0" stop-color="#6aab32"/><stop offset="1" stop-color="#4d8f22"/>
      </linearGradient>
    </defs>
    <rect role="img" aria-label="Sheep grazing on a grassy ridge under a blue sky with clouds" width="542" height="175" fill="url(#backSky)"/>
    <rect y="172" width="542" height="466" fill="url(#backField)"/>
  </svg>

  <div class="brand">
    <span class="brand__mark"></span>
    <span class="brand__name">Northcliff Thermal<br>Services Ltd</span>
  </div>

  <div class="back-copy">
    <p>DWB payments are paid by the Government for 7 years every quarter directly into your bank to offset the initial cost of equipment.</p>
    <p>Ongoing savings year on year of 50% compared to your current fuel usage. Saving between £500 and £1200</p>
    <p>Heat pumps require little maintenance and have a life expectancy of 25+ years; where after just the main unit would have to be replaced, making replacement expectation similar to a standard boiler.</p>
    <p>In October of 2014 the Government finalised the groundbreaking DWB domestic warmth bonus. We are the first country in the world to give payments to cover the install cost of renewable technology based around heating and hot water.</p>
    <p>At Northcliff Thermal Services we are in a unique position to advise you on the options open to you to replace your Oil and LPG boilers in favour of products that are 50% cheaper to run and are also kinder to the environment.</p>
    <p>We have 15 years experience in the Renewable Energy market and are not tied to one supplier or one technology. This puts us in a position to discuss ALL the options that are open to you to enable you to make a correct informed decision.</p>
    <p>We are able to manage your project from start to finish and ongoing servicing; with a staff of 20 we do not sub our work to other contractors allowing us to give the end user confidence and peace of mind before, during and after install.</p>
    <p>Please get in touch and we are happy to give free impartial advice on options open to you.</p>
    <p>Call our Plymouth based office and asks to speak to Owen our Energy Consultant or Dale</p>
  </div>

  <div class="back-footer">
    <div class="back-url">www.ncthermal.co.uk</div>
    <div class="partners">
      <svg class="partner" width="52" height="30"><rect width="52" height="30" rx="3" fill="#f2a33a"/></svg>
      <svg class="partner" width="34" height="30"><circle cx="17" cy="15" r="14" fill="#9fb7c9"/></svg>
      <svg class="partner" width="30" height="30"><rect width="30" height="30" fill="#2b3f8f"/></svg>
      <svg class="partner" width="100" height="26"><rect width="100" height="26" rx="3" fill="#2a63b0"/></svg>
      <svg class="partner" width="62" height="30"><rect width="62" height="30" fill="#e2231a"/></svg>
      <svg class="partner" width="96" height="32"><rect width="96" height="32" rx="16" fill="#1f3466"/></svg>
    </div>
  </div>
</section>

</body>
</html>
```